Artificial intelligence, machine learning, and automation company needs a sexy business card design

We need a sleek and sexy business card design for an AI consulting company based in Philadelphia PA. We provide custom machine learning and automation solutions for companies of all shapes and sizes. The primary industries that we serve are pharmaceuticals, engineering, healthcare, and computer software. We would like the designs to be a black business card that uses green as a sleek accent color. The final design should communicate intelligence, cutting edge new-tech, and optimization.

Target Market(s)

C-level and VP level executives of multi-million annual companies. Mostly in Pharma, Healthcare, Real Estate, Retail, and Engineering

Industry/Entity Type

Computer Software

Contact Information for Business Card

Name: Jack Moss
Title: CEO
Cell: 215 604 8293
Email: JackM@quillarcworks.example
Website: www.QuillarcWorks.example

Font styles to use
Sans Serif

Colors

Designer to choose colors to be used in the design.

Requirements
Must have
• 1) Attached Quillarc Logo (either with colors or not/embossed)
• 2) "Artificial Intelligence" "Automation" and "Machine Learning"
• 3) "Quillarc Laboratories" or "Quillarc Works" or "Quillarc"
• 4) Sexy AF.
Nice to have
• Black card / dark card color, "Quillarc Green" accent colors (in attached .ai file), Embossment of logo/name/etc, thick card stock, colored borders (on card sides, not front/back faces)
Should not have
• Should not be bland, or unsexy.

```html
<!DOCTYPE html>
<html lang="en">
<head>
<meta charset="utf-8">
<title>Quillarc Laboratories – Business Card</title>
<link rel="stylesheet" href="https://fonts.googleapis.com/css2?family=Roboto:wght@400;500;700&display=swap">
<style>
  :root {
    --stage: #1c1d1f;
    --card-dark: #1b1b1c;
    --card-light: #eeeeec;
    --quillarc-green: #4fd1b8;
    --ink: #1a1a1a;
    --text-light: #d9d9d9;
    --text-muted: #a9a9a9;
  }
  * { box-sizing: border-box; margin: 0; padding: 0; }
  html, body {
    width: 1200px; height: 900px; overflow: hidden;
    background: var(--stage);
    font-family: "Roboto", sans-serif;
  }
  .stage {
    position: relative; width: 1200px; height: 900px;
    display: flex; flex-direction: column; align-items: center; justify-content: center; gap: 48px;
  }
  .card {
    position: relative; width: 580px; height: 332px;
    box-shadow: 0 12px 30px rgba(0,0,0,.45);
  }
  .card--back { background: var(--card-light); }
  .card--front { background: var(--card-dark); }

  .wordmark {
    display: flex; align-items: center; gap: 16px;
    font-family: "Roboto", sans-serif; font-weight: 400; text-transform: uppercase;
  }
  .wordmark__square { width: 22px; height: 22px; flex: none; }
  .wordmark__name { display: flex; flex-direction: column; line-height: 1.1; }
  .wordmark__main { font-size: 34px; letter-spacing: 9px; }
  .wordmark__sub { font-size: 13px; letter-spacing: 5.5px; }

  .card--back .wordmark {
    position: absolute; left: 50%; top: 50%; transform: translate(-50%, -50%);
    color: var(--ink);
  }
  .card--back .wordmark__square { background: var(--ink); }

  .contact {
    position: absolute; left: 46px; top: 44px;
    list-style: none; display: flex; flex-direction: column; gap: 8px;
  }
  .contact__item {
    display: flex; align-items: center; gap: 10px;
    font-size: 17px; font-weight: 500; color: var(--text-light);
  }
  .contact__icon { width: 16px; height: 16px; flex: none; }

  .person { position: absolute; left: 46px; top: 150px; }
  .person__name { font-size: 40px; font-weight: 700; color: var(--quillarc-green); letter-spacing: -0.5px; }
  .person__title { font-size: 14px; font-weight: 400; color: var(--text-muted); margin-top: 2px; }

  .card--front .wordmark {
    position: absolute; right: 36px; bottom: 34px;
    color: var(--quillarc-green); gap: 12px;
  }
  .card--front .wordmark__square { width: 16px; height: 16px; background: var(--quillarc-green); }
  .card--front .wordmark__main { font-size: 24px; letter-spacing: 6px; }
  .card--front .wordmark__sub { font-size: 9.5px; letter-spacing: 3.8px; }
</style>
</head>
<body>
<main class="stage">
  <section class="card card--back" aria-label="Card back">
    <div class="wordmark">
      <span class="wordmark__square"></span>
      <span class="wordmark__name">
        <span class="wordmark__main">Quillarc</span>
        <span class="wordmark__sub">Laboratories</span>
      </span>
    </div>
  </section>

  <section class="card card--front" aria-label="Card front">
    <ul class="contact">
      <li class="contact__item">
        <svg class="contact__icon" viewBox="0 0 16 16" aria-hidden="true">
          <rect width="16" height="16" rx="2" fill="#4fd1b8"/>
          <path d="M3 5h10v7H3z M3 5l5 4 5-4" fill="none" stroke="#1b1b1c" stroke-width="1.4"/>
        </svg>
        JackM@quillarcworks.example
      </li>
      <li class="contact__item">
        <svg class="contact__icon" viewBox="0 0 16 16" aria-hidden="true">
          <rect width="16" height="16" rx="2" fill="#4fd1b8"/>
          <path d="M5 3.5l2 2.2-1.2 1.5c.7 1.4 1.6 2.3 3 3l1.5-1.2 2.2 2-1.3 1.6C7.5 12.4 3.6 8.5 3.4 4.8z" fill="#1b1b1c"/>
        </svg>
        215 604 8293
      </li>
      <li class="contact__item">
        <svg class="contact__icon" viewBox="0 0 16 16" aria-hidden="true">
          <circle cx="8" cy="8" r="7.5" fill="#4fd1b8"/>
          <circle cx="8" cy="8" r="4.5" fill="none" stroke="#1b1b1c" stroke-width="1.2"/>
          <path d="M3.5 8h9 M8 3.5c-2 2.5-2 6.5 0 9 M8 3.5c2 2.5 2 6.5 0 9" fill="none" stroke="#1b1b1c" stroke-width="1"/>
        </svg>
        www.QuillarcWorks.example
      </li>
    </ul>

    <div class="person">
      <p class="person__name">Jack Moss</p>
      <p class="person__title">CEO</p>
    </div>

    <div class="wordmark">
      <span class="wordmark__square"></span>
      <span class="wordmark__name">
        <span class="wordmark__main">Quillarc</span>
        <span class="wordmark__sub">Laboratories</span>
      </span>
    </div>
  </section>
</main>
</body>
</html>
```